Book Cover for 'Mira Kept a Lantern'

I need a book cover for my novel. The story is set in the ancient Greece of Dorvan, and is a retelling of a story from the Velmorid. Clytemnestra's husband, Agamemnon, is the paramount king in Greece. When his sister in law Helen runs away to Troy with Paris, Agamemnon summons the Greek army to attack Troy and win her back. To ensure the right winds blow for his fleet to sail to Troy, Agamemnon sacrifices his eldest daughter. Clytemnestra takes revenge by murdering Agamemnon when he returns from conquering Troy. She is in turn murdered by their son Orestes a few years later to avenge his father's death.

I would like a cover which reflects the ancient Greek setting - I wondered whether a motif based on the artwork found on ancient Greek pottery might be appropriate, but I am open to other suggestions. Although the core of the story involve the daughter's murder, and the revenge killing of her husband, this is Clytemnestra's story and I want to present her as a great queen who rules a kingdom well in her husband's absence. The tradition in Greece was for women to be sequestered, but Clytemnestra comes from Sparta, a kingdom with greater freedom for women and a greater respect for them.

Although the time period and story are very different from my first novel, I would like this cover to convey that my latest book is by the same author and part of an ongoing body of work so that there is a sort of brand recognition. So some common denominator would be good

```html
<!DOCTYPE html>
<html lang="en">
<head>
<meta charset="utf-8">
<title>Mira Kept a Lantern — Book Cover</title>
<link rel="stylesheet" href="https://fonts.googleapis.com/css2?family=Caesar+Dressing&family=Arimo:wght@400&display=swap">
<style>
  :root {
    --parchment-light: #f4cf7e;
    --parchment-mid: #e9a647;
    --parchment-deep: #c9702a;
    --frieze-ground: #d9a565;
    --frieze-dark: #6e2a12;
    --frieze-rule: #8b3517;
    --ink: #140c08;
  }
  * { margin: 0; padding: 0; box-sizing: border-box; }
  html, body { width: 800px; height: 1200px; overflow: hidden; }
  body { background: var(--parchment-mid); }

  .cover {
    position: relative;
    width: 800px;
    height: 1200px;
    overflow: hidden;
    background:
      radial-gradient(ellipse 60% 40% at 50% 45%, var(--parchment-light) 0%, rgba(244,207,126,0) 70%),
      radial-gradient(ellipse 80% 60% at 20% 80%, rgba(201,112,42,0.55) 0%, rgba(201,112,42,0) 70%),
      radial-gradient(ellipse 70% 50% at 85% 20%, rgba(201,112,42,0.45) 0%, rgba(201,112,42,0) 70%),
      linear-gradient(160deg, var(--parchment-mid), var(--parchment-light) 45%, var(--parchment-mid) 75%, var(--parchment-deep));
  }

  .frieze {
    position: absolute;
    left: 0;
    width: 800px;
    height: 96px;
    background: linear-gradient(180deg, var(--frieze-ground), #c98b4c);
  }
  .frieze::before {
    content: "";
    position: absolute;
    left: 0; right: 0;
    height: 16px;
    background: var(--frieze-rule);
  }
  .frieze--top { top: 0; }
  .frieze--top::before { top: 0; }
  .frieze--bottom { bottom: 0; }
  .frieze--bottom::before { bottom: 0; }

  .title {
    position: absolute;
    top: 262px;
    left: 0;
    width: 800px;
    text-align: center;
    font-family: "Caesar Dressing", "Trebuchet MS", sans-serif;
    font-weight: 400;
    color: var(--ink);
    text-transform: uppercase;
    letter-spacing: 4px;
  }
  .title__line {
    display: block;
    line-height: 1;
  }
  .title__line--lead { font-size: 184px; }
  .title__line--middle { font-size: 184px; margin-top: 6px; }
  .title__line--last { font-size: 132px; margin-top: 70px; }

  .author {
    position: absolute;
    top: 990px;
    left: 0;
    width: 800px;
    text-align: center;
    font-family: "Arimo", Arial, sans-serif;
    font-size: 48px;
    color: var(--ink);
  }
</style>
</head>
<body>
  <main class="cover">
    <div class="frieze frieze--top" role="img" aria-label="Frieze of ancient Greek pottery figures in black on terracotta"></div>

    <h1 class="title">
      <span class="title__line title__line--lead">Mira</span>
      <span class="title__line title__line--middle">Kept A</span>
      <span class="title__line title__line--last">Lantern</span>
    </h1>

    <p class="author">Author’s Name</p>

    <div class="frieze frieze--bottom" role="img" aria-label="Frieze of ancient Greek pottery figures in black on terracotta"></div>
  </main>
</body>
</html>
```